Business Reporting Graph Illustration

I'm looking for a graphic design to created an illustration of a line chart I have two sample charts that I'd like elements of each combined together to create the project. Below is a link to learn more about this project. This should be designed using any product of the Adobe Suite.
Color Scheme is included within the below link. This will require 2 - 3 rounds of design before final completion.

https://www.plonvadesk.com/file/QWT8HbxuLeMRa302KD5Vpt/Graphic-Design-Project

```html
<!DOCTYPE html>
<html lang="en">
<head>
<meta charset="utf-8">
<title>Business Reporting Graph</title>
<link href="https://fonts.googleapis.com/css2?family=Montserrat:wght@400;500&display=swap" rel="stylesheet">
<style>
  :root {
    --bg: #ffffff;
    --series-main: #0d1b3e;
    --series-baseline: #5b7fb0;
    --ad-marker: #f9b233;
    --axis: #9a9a9a;
    --axis-label: #8c8c8c;
  }
  html, body {
    margin: 0;
    padding: 0;
    width: 1200px;
    height: 675px;
    overflow: hidden;
    background: var(--bg);
  }
  .chart {
    display: block;
    width: 1200px;
    height: 675px;
    font-family: "Montserrat", sans-serif;
  }
  .ad-line { stroke: var(--ad-marker); stroke-width: 2; stroke-dasharray: 9 7; fill: none; }
  .ad-tag rect { fill: var(--bg); stroke: var(--ad-marker); stroke-width: 2; }
  .ad-tag text { fill: var(--ad-marker); font-size: 16px; font-weight: 500; text-anchor: middle; }
  .axis-line { stroke: var(--axis); stroke-width: 2; }
  .axis-tick { stroke: var(--axis); stroke-width: 2; }
  .axis-label { fill: var(--axis-label); font-size: 16px; text-anchor: middle; }
  .series-baseline { stroke: var(--series-baseline); stroke-width: 3; fill: none; stroke-linecap: round; }
  .series-main { stroke: var(--series-main); stroke-width: 3; fill: none; stroke-linejoin: round; stroke-linecap: round; }
</style>
</head>
<body>
<svg class="chart" viewBox="0 0 1920 1080" role="img" aria-label="Line chart of traffic from 10:30 am to 2:15 pm with spikes during TV ad slots">
  <g class="ad-markers">
    <line class="ad-line" x1="122" y1="130" x2="122" y2="882"/>
    <line class="ad-line" x1="146" y1="130" x2="146" y2="882"/>
    <line class="ad-line" x1="872" y1="130" x2="872" y2="882"/>
    <line class="ad-line" x1="912" y1="130" x2="912" y2="882"/>
    <line class="ad-line" x1="1330" y1="130" x2="1330" y2="882"/>
    <line class="ad-line" x1="1410" y1="130" x2="1410" y2="882"/>
  </g>

  <g class="ad-tag">
    <rect x="89" y="160" width="90" height="50"/>
    <text x="134" y="180">TV Ad</text>
    <text x="134" y="199">(3 Min)</text>
  </g>
  <g class="ad-tag">
    <rect x="847" y="160" width="90" height="50"/>
    <text x="892" y="180">TV Ad</text>
    <text x="892" y="199">(5 Min)</text>
  </g>
  <g class="ad-tag">
    <rect x="1325" y="160" width="90" height="50"/>
    <text x="1370" y="180">TV Ad</text>
    <text x="1370" y="199">(10 Min)</text>
  </g>

  <g class="baseline-series">
    <path class="series-baseline" d="M180,808 C185,800 187,785 193,785 C200,785 205,805 220,812 C232,818 245,812 258,810 C268,808 275,812 280,818"/>
    <path class="series-baseline" d="M870,800 C880,790 887,762 895,762 C903,762 908,812 918,814 C925,815 935,785 945,786 C950,787 955,798 958,805"/>
    <path class="series-baseline" d="M1335,790 C1345,788 1350,788 1358,793 C1365,797 1372,797 1380,788 C1388,780 1400,778 1410,785 C1420,792 1428,795 1440,789 L1462,781"/>
  </g>

  <path class="series-main" d="M68,815 C90,822 105,828 118,827 C130,826 135,818 148,819 C160,818 170,825 178,812 C185,795 186,752 198,752 C210,752 225,772 240,785 C255,798 265,800 280,815 C292,828 300,832 310,832 C325,834 330,845 340,850 C350,854 355,848 360,842 L410,792 C420,784 428,790 435,800 L462,836 C470,843 480,842 488,833 C500,816 505,800 512,775 C518,752 522,750 527,770 L543,830 C548,840 553,832 558,820 C565,803 572,798 582,798 C592,800 605,810 620,815 L648,805 L682,835 C690,842 698,840 704,828 C712,810 718,803 730,803 C740,804 750,820 765,825 C775,828 782,822 800,821 C820,820 850,825 862,810 C870,800 872,780 875,740 L894,350 L912,660 C915,720 915,745 925,760 C940,770 948,780 958,805 C962,815 968,820 972,810 C980,788 985,755 1000,754 C1012,754 1022,770 1028,785 L1045,838 C1050,846 1055,840 1060,830 C1066,815 1070,810 1077,812 C1085,816 1090,845 1098,843 C1106,840 1112,808 1120,800 C1128,792 1135,794 1145,800 C1160,808 1170,820 1185,818 C1200,815 1205,810 1220,809 C1240,808 1250,813 1265,813 C1290,814 1320,805 1335,790 C1345,780 1346,770 1350,750 L1370,232 L1410,640 C1415,700 1418,745 1425,758 C1435,785 1450,782 1462,781 C1475,781 1480,793 1490,795 C1500,797 1510,783 1520,788 C1530,792 1532,805 1545,815 C1555,825 1570,830 1580,815 C1590,795 1600,786 1612,786 C1625,788 1632,797 1645,802 C1660,806 1670,803 1685,797 C1695,792 1705,793 1712,794 C1725,795 1730,778 1735,760 C1742,735 1745,722 1750,728 L1772,820 L1797,722 C1802,720 1805,730 1812,760 C1820,792 1825,797 1840,797 L1868,789"/>

  <g class="time-axis">
    <line class="axis-line" x1="63" y1="882" x2="1863" y2="882"/>
    <g class="axis-ticks">
      <line class="axis-tick" x1="63" y1="872" x2="63" y2="892"/>
      <line class="axis-tick" x1="183" y1="872" x2="183" y2="892"/>
      <line class="axis-tick" x1="303" y1="872" x2="303" y2="892"/>
      <line class="axis-tick" x1="423" y1="872" x2="423" y2="892"/>
      <line class="axis-tick" x1="543" y1="872" x2="543" y2="892"/>
      <line class="axis-tick" x1="663" y1="872" x2="663" y2="892"/>
      <line class="axis-tick" x1="783" y1="872" x2="783" y2="892"/>
      <line class="axis-tick" x1="903" y1="872" x2="903" y2="892"/>
      <line class="axis-tick" x1="1023" y1="872" x2="1023" y2="892"/>
      <line class="axis-tick" x1="1143" y1="872" x2="1143" y2="892"/>
      <line class="axis-tick" x1="1263" y1="872" x2="1263" y2="892"/>
      <line class="axis-tick" x1="1383" y1="872" x2="1383" y2="892"/>
      <line class="axis-tick" x1="1503" y1="872" x2="1503" y2="892"/>
      <line class="axis-tick" x1="1623" y1="872" x2="1623" y2="892"/>
      <line class="axis-tick" x1="1743" y1="872" x2="1743" y2="892"/>
      <line class="axis-tick" x1="1863" y1="872" x2="1863" y2="892"/>
    </g>
    <g class="axis-labels">
      <text class="axis-label" x="63" y="917">10:30 am</text>
      <text class="axis-label" x="183" y="917">10:45 am</text>
      <text class="axis-label" x="303" y="917">11:00 am</text>
      <text class="axis-label" x="423" y="917">11:15 am</text>
      <text class="axis-label" x="543" y="917">11:30 am</text>
      <text class="axis-label" x="663" y="917">11:45 am</text>
      <text class="axis-label" x="783" y="917">12:00 pm</text>
      <text class="axis-label" x="903" y="917">12:15 pm</text>
      <text class="axis-label" x="1023" y="917">12:30 pm</text>
      <text class="axis-label" x="1143" y="917">12:45 pm</text>
      <text class="axis-label" x="1263" y="917">1:00 pm</text>
      <text class="axis-label" x="1383" y="917">1:15 am</text>
      <text class="axis-label" x="1503" y="917">1:30 pm</text>
      <text class="axis-label" x="1623" y="917">1:45 pm</text>
      <text class="axis-label" x="1743" y="917">2:00 pm</text>
      <text class="axis-label" x="1863" y="917">2:15 pm</text>
    </g>
  </g>
</svg>
</body>
</html>
```